Below Par Parenting

I would like a poster (size to be agreed) created for the wording that I have composed and which I have pasted below. The poster is for my own personal gratification. It is not for commercial use. The message is driven by honesty and a profound sense of mea culpa. I am open to ideas regarding style and presentation.
I am an awful parent. No question. I am not cut out for this shit. I’m too quick to temper. I turn everything into a test of wills. I’m not down for food on the floor, for having my car trashed with your stink and detritus, for having the walls of my house daubed in your greasy fingerprints. I want to listen to The Marrows not Bumble Over Dewfields on repeat. I enjoyed making you but, on reflection, I should have pulled out. Let me go back in time to that great waste of space and energy that is ante-natal classes and tell that boho with the flowery dress and curly hair, ‘Why are you concentrating on the first five seconds? All the pain comes later. Why aren’t you telling us what to do when they won’t sleep, when they won’t sit in their high chairs, when they won’t sleep on the aeroplane?’ Boy, I wish I could play it loosey-goosey like those left-leaning parents I see going ‘coo-coo’ in Brindisetti’s but I’m not built like that. I am a right-wing despot. It’s Nazi Germany back at my place. I’m not interested in your meltdowns and tantrums. You want to writhe on the floor in the car park going red in the face? Make my day. You want to go spastic because I won’t let you watch TV for five hours straight? I don’t give a shit. Read my lips. I won’t pander to it. My wife says you’re babies but all I see is little people with an agenda. I’ve got naughty steps and sin-bins all over the joint. I wish I wasn’t the tyrant, the Valdrumo and the Oko Temba I am but it is what it is. I blame my parents and they, in turn, will blame me and their parents. Understand I don’t want to infect you too much with my bad behavior but if you could stop making such a scene in public places with your screaming, your bitching and your all round refusal to play nice then maybe, just maybe, we’d have a chance and I wouldn’t be such an awful parent.

```html
<!DOCTYPE html>
<html lang="en">
<head>
<meta charset="utf-8">
<title>Below Par Parenting</title>
<link rel="stylesheet" href="https://fonts.googleapis.com/css2?family=Archivo:wdth,wght@62..125,800&display=swap">
<style>
  :root {
    --paper: #ffffff;
    --ink: #111111;
  }
  * { margin: 0; padding: 0; box-sizing: border-box; }
  html, body {
    width: 853px;
    height: 1200px;
    overflow: hidden;
    background: var(--paper);
  }
  .poster {
    display: block;
    width: 853px;
    height: 1200px;
    background: var(--paper);
  }
  .confession {
    fill: var(--ink);
    font-family: "Archivo", "Helvetica Neue", Arial, sans-serif;
    font-weight: 800;
    font-stretch: 80%;
    text-transform: uppercase;
  }
  .confession--wide { font-stretch: 110%; }
  .confession--narrow { font-stretch: 68%; }
</style>
</head>
<body>
<svg class="poster" viewBox="0 0 853 1200" role="img" aria-label="I am an awful parent">
  <g class="column">
    <text class="confession confession--wide" x="88" y="113" font-size="44" textLength="680" lengthAdjust="spacingAndGlyphs">I am an awful parent.</text>
    <text class="confession confession--wide" x="88" y="167" font-size="65" textLength="680" lengthAdjust="spacingAndGlyphs">No question.</text>
    <text class="confession" x="88" y="206" font-size="39" textLength="680" lengthAdjust="spacingAndGlyphs">I am not cut out for this shit.</text>
    <text class="confession confession--wide" x="88" y="249" font-size="42" textLength="680" lengthAdjust="spacingAndGlyphs">I’m too quick to temper.</text>

    <text class="confession" x="88" y="281" font-size="21" textLength="680" lengthAdjust="spacingAndGlyphs">I turn everything into a test of wills. I’m not down</text>
    <text class="confession" x="88" y="302" font-size="21" textLength="680" lengthAdjust="spacingAndGlyphs">for food on the floor, for having my car trashed</text>
    <text class="confession" x="88" y="323" font-size="21" textLength="680" lengthAdjust="spacingAndGlyphs">with your stink and detritus, for having the walls</text>
    <text class="confession" x="88" y="344" font-size="21" textLength="680" lengthAdjust="spacingAndGlyphs">of my house daubed in your greasy fingerprints.</text>

    <text class="confession" x="88" y="403" font-size="38" textLength="680" lengthAdjust="spacingAndGlyphs">I want to listen to The Marrows</text>
    <text class="confession confession--narrow" x="88" y="438" font-size="38" textLength="680" lengthAdjust="spacingAndGlyphs">not Bumble Over Dewfields on repeat.</text>
    <text class="confession" x="88" y="470" font-size="32" textLength="680" lengthAdjust="spacingAndGlyphs">I enjoyed making you but, on reflection,</text>
    <text class="confession" x="88" y="510" font-size="46" textLength="680" lengthAdjust="spacingAndGlyphs">I should have pulled out.</text>

    <text class="confession" x="88" y="527" font-size="12" textLength="680" lengthAdjust="spacingAndGlyphs">Let me go back in time to that great waste of space and energy that is ante-natal classes</text>
    <text class="confession" x="88" y="551" font-size="21" textLength="680" lengthAdjust="spacingAndGlyphs">and tell that boho with the flowery dress and curly hair,</text>
    <text class="confession" x="88" y="578" font-size="28" textLength="680" lengthAdjust="spacingAndGlyphs">‘Why are you concentrating on the first five</text>
    <text class="confession" x="88" y="605" font-size="28" textLength="680" lengthAdjust="spacingAndGlyphs">seconds? All the pain comes later. Why aren’t</text>
    <text class="confession" x="88" y="631" font-size="28" textLength="680" lengthAdjust="spacingAndGlyphs">you telling us what to do when they won’t</text>
    <text class="confession" x="88" y="657" font-size="28" textLength="680" lengthAdjust="spacingAndGlyphs">sleep, when they won’t sit in their high chairs,</text>
    <text class="confession" x="88" y="683" font-size="28" textLength="680" lengthAdjust="spacingAndGlyphs">when they won’t sleep on the aeroplane?’</text>

    <text class="confession" x="88" y="699" font-size="17" textLength="680" lengthAdjust="spacingAndGlyphs">Boy, I wish I could play it loosey-goosey like those left-leaning</text>
    <text class="confession" x="88" y="717" font-size="17" textLength="680" lengthAdjust="spacingAndGlyphs">parents I see going ‘coo-coo’ in Brindisetti’s but I’m not built like that.</text>

    <text class="confession" x="88" y="757" font-size="40" textLength="680" lengthAdjust="spacingAndGlyphs">I am a right-wing despot. It’s</text>
    <text class="confession" x="88" y="790" font-size="40" textLength="680" lengthAdjust="spacingAndGlyphs">Nazi Germany back at my place.</text>
    <text class="confession" x="88" y="826" font-size="44" textLength="680" lengthAdjust="spacingAndGlyphs">I’m not interested in your</text>
    <text class="confession" x="88" y="860" font-size="44" textLength="680" lengthAdjust="spacingAndGlyphs">meltdowns and tantrums.</text>

    <text class="confession" x="88" y="882" font-size="18" textLength="680" lengthAdjust="spacingAndGlyphs">You want to writhe on the floor in the car park going red</text>
    <text class="confession" x="88" y="900" font-size="18" textLength="680" lengthAdjust="spacingAndGlyphs">in the face? Make my day. You want to go spastic because I</text>
    <text class="confession confession--narrow" x="88" y="925" font-size="25" textLength="680" lengthAdjust="spacingAndGlyphs">won’t let you watch TV for five hours straight?</text>
    <text class="confession confession--narrow" x="88" y="950" font-size="25" textLength="680" lengthAdjust="spacingAndGlyphs">I don’t give a shit. Read my lips. I won’t pander to it.</text>
    <text class="confession confession--narrow" x="88" y="961" font-size="9" textLength="680" lengthAdjust="spacingAndGlyphs">My wife says you’re babies but all I see is little people with an agenda. I’ve got naughty steps and sin-bins all over the joint.</text>

    <text class="confession" x="88" y="991" font-size="30" textLength="680" lengthAdjust="spacingAndGlyphs">I wish I wasn’t the tyrant, the Valdrumo</text>
    <text class="confession" x="88" y="1021" font-size="30" textLength="680" lengthAdjust="spacingAndGlyphs">and the Oko Temba I am but it is what it is.</text>
    <text class="confession" x="88" y="1040" font-size="17" textLength="680" lengthAdjust="spacingAndGlyphs">I blame my parents and they, in turn, will blame me and their parents.</text>
    <text class="confession confession--narrow" x="88" y="1059" font-size="16" textLength="680" lengthAdjust="spacingAndGlyphs">Understand I don’t want to infect you too much with my bad behavior but if you could</text>
    <text class="confession confession--narrow" x="88" y="1078" font-size="16" textLength="680" lengthAdjust="spacingAndGlyphs">stop making such a scene in public places with your screaming, your bitching and</text>
    <text class="confession confession--narrow" x="88" y="1097" font-size="16" textLength="680" lengthAdjust="spacingAndGlyphs">your all round refusal to play nice then maybe, just maybe, we’d have a chance</text>
    <text class="confession" x="88" y="1126" font-size="30" textLength="680" lengthAdjust="spacingAndGlyphs">and I wouldn’t be such an awful parent.</text>
  </g>
</svg>
</body>
</html>
```